WordPress website design for wealth management company

A modern clean look website for a service company. This is mostly for information only, with a form to capture prospect contact information and schedule a 15 minutes call. There will be several static pages describe what services we offer, how we are different, and a blog section for posting articles and share resources. A section for client testimonials.
I want a website that is easy to understand and maintain. No proprietary plugins that cost extra. The main thing I need help is the visual layout / color palette that present a clean and professional look, select the suitable stock photos that convey the image of trust, professional, innovative, and high service.
Some websites with style I like include the following
- https://www.halbrookwealth.com/
- https://www.morvatefinancialorbits.com/
- https://tamblinfunds.com/private-equity-partners/
Also some websites in other industries with clean modern look
- https://plorvix.com/
- https://gravola.com/
- https://www.brisotelka.com/
I want the end product to be a fully functional website that I can upload into web hosting service I use and I can easily add content and maintain myself in the future.

```html
<!DOCTYPE html>
<html lang="en">
<head>
<meta charset="utf-8">
<title>Brantmoor Wealth</title>
<link href="https://fonts.googleapis.com/css2?family=Libre+Franklin:wght@400;500;600;700;800&display=swap" rel="stylesheet">
<style>
:root{
  --purple:#5b2a91;
  --purple-dark:#3f1a6e;
  --gold:#fbb832;
  --lavender:#f1ecfa;
  --ink:#2b2b2b;
  --muted:#555;
  --footer:#121212;
  --white:#fff;
}
*{margin:0;padding:0;box-sizing:border-box}
html,body{width:1200px;height:4383px;overflow:hidden}
body{position:relative;font-family:"Libre Franklin",Arial,sans-serif;color:var(--ink);background:var(--white)}
.abs{position:absolute}
.btn{position:absolute;display:flex;align-items:center;justify-content:center;background:var(--gold);color:var(--white);font-weight:600;font-size:15px;border-radius:20px;text-transform:uppercase}
.eyebrow{font-size:13px;letter-spacing:6px;color:var(--purple);text-transform:uppercase;text-align:center}
.section-title{font-size:36px;font-weight:800;text-align:center;text-transform:uppercase;color:var(--ink)}
.center{left:0;width:1200px}

/* header */
.topbar{left:262px;top:0;width:938px;height:34px;background:var(--purple);clip-path:polygon(0 0,100% 0,100% 100%,50px 100%);display:flex;justify-content:flex-end;align-items:center;gap:22px;padding-right:92px;color:var(--white);font-size:15px;font-weight:500}
.topbar span{display:flex;align-items:center;gap:6px}
.brand{left:99px;top:10px;display:flex;align-items:center;gap:10px}
.brand-mark{width:46px;height:46px;border-radius:50%;background:var(--gold)}
.brand-name{font-size:22px;font-weight:700;letter-spacing:3px;color:var(--purple);line-height:1}
.nav{left:467px;top:58px;display:flex;gap:42px;font-size:15px;font-weight:500;color:var(--ink)}
.nav .active{color:var(--purple);border-bottom:2px solid var(--purple);padding-bottom:4px}
.nav-cta{left:953px;top:48px;width:147px;height:38px}

/* hero */
.hero{left:0;top:100px;width:1200px;height:627px;background:linear-gradient(110deg,#8e8a84 0%,#c9c2b8 30%,#3b3f4a 55%,#e6ddd2 80%,#b3a79b 100%)}
.hero-title{left:100px;top:330px;font-size:36px;font-weight:500;color:var(--white)}
.hero-text{left:100px;top:385px;width:360px;font-size:13px;line-height:24px;color:var(--white)}
.hero-btn{left:102px;top:448px;width:188px;height:38px}
.form{left:748px;top:204px;width:350px;height:422px;background:rgba(91,42,145,.85)}
.form-head{height:40px;display:flex;align-items:center;justify-content:center;color:var(--white);font-weight:600;font-size:18px;background:var(--purple)}
.field{position:absolute;left:14px;width:322px;height:40px;background:var(--white);border-radius:3px;font-size:12px;color:#666;padding:12px 12px}
.dots{left:555px;top:685px;display:flex;gap:14px}
.dots i{display:block;width:11px;height:11px;border:1.5px solid var(--white);border-radius:50%}
.dots i.on{background:var(--white)}

/* about */
.about-img{left:99px;top:793px;width:483px;height:421px;border-radius:0 40px 0 40px;background:linear-gradient(160deg,#2b2f36 0%,#8fa070 55%,#cfc8bb 100%);box-shadow:6px 8px 0 var(--purple)}
.about-copy{left:647px;top:826px;width:455px}
.about-copy .eyebrow{text-align:left}
.about-copy h2{font-size:36px;font-weight:800;line-height:38px;margin:10px 0 14px;text-transform:uppercase}
.about-copy p{font-size:14px;line-height:26px;color:var(--muted);margin-bottom:12px}
.about-btn{left:649px;top:1141px;width:157px;height:38px}

/* services */
.services{left:0;top:1280px;width:1200px;height:507px;background:var(--lavender)}
.svc{position:absolute;top:133px;width:238px;height:250px;background:var(--white);box-shadow:0 3px 10px rgba(0,0,0,.08);text-align:center}
.svc .icon{width:60px;height:60px;margin:20px auto 10px;border-radius:50%;background:#e8def6}
.svc h3{font-size:18px;font-weight:600;margin-bottom:10px}
.svc p{font-size:12px;line-height:23px;color:var(--muted);padding:0 16px}
.svc .go{position:absolute;right:0;bottom:0;width:44px;height:40px;background:var(--gold);border-radius:22px 0 0 0}
.arrow{position:absolute;top:252px}
.all-btn{left:490px;top:410px;width:219px;height:39px;background:var(--purple)}

/* cta */
.cta{left:0;top:1787px;width:1200px;height:499px;background:linear-gradient(90deg,#a9a9a7 0%,#d7d2cb 35%,#28324a 65%,#e9e3da 100%)}
.cta-circle{left:167px;top:34px;width:442px;height:442px;border-radius:50%;background:var(--purple);border:7px solid var(--gold);border-left-color:var(--purple);border-top-color:var(--purple);text-align:center;padding-top:155px}
.cta-circle .eyebrow{color:var(--white);font-size:12px}
.cta-circle h2{font-size:36px;font-weight:700;color:var(--white);line-height:44px;margin-top:10px}
.cta-btn{left:124px;top:333px;width:188px;height:38px}

/* who we serve */
.serve{position:absolute;top:2434px;width:234px;height:327px}
.serve h3{position:absolute;left:16px;top:224px;font-size:18px;font-weight:700;color:var(--white);line-height:22px;text-transform:uppercase}
.serve p{position:absolute;left:16px;top:274px;width:210px;font-size:12px;line-height:22px;color:var(--white)}

/* testimonials */
.testi{left:0;top:2834px;width:1200px;height:482px;background:var(--lavender)}
.tcard{position:absolute;top:148px;width:312px;height:269px;background:var(--white)}
.tcard .q{position:absolute;left:20px;top:-16px;width:48px;height:48px;border-radius:50%;background:var(--purple-dark);color:var(--white);font-size:40px;font-weight:800;text-align:center;line-height:58px}
.tcard h4{position:absolute;left:20px;top:58px;font-size:17px;font-weight:700}
.tcard small{position:absolute;left:20px;top:80px;font-size:9px;color:#777}
.tcard p{position:absolute;left:20px;top:106px;width:272px;font-size:14px;line-height:27px;color:var(--muted);text-align:justify}

/* blog */
.blog-main{left:102px;top:3464px;width:477px;height:459px;background:var(--white);box-shadow:0 2px 10px rgba(0,0,0,.12)}
.blog-main .ph{height:274px;border-radius:0 0 40px 0;background:linear-gradient(180deg,#e9e6e1 0%,#4b4f5a 70%,#cfc9c1 100%)}
.blog-main .body{padding:18px 24px}
.date{font-size:12px;color:#666}
.blog-main h3{font-size:18px;font-weight:700;line-height:24px;margin:10px 0 6px}
.blog-main p{font-size:13px;line-height:21px;color:var(--muted)}
.more{display:inline-block;font-size:13px;font-weight:700;color:var(--purple-dark);border-bottom:2px solid var(--gold);padding-bottom:2px;margin-top:8px}
.blog-sm{position:absolute;left:621px;width:477px;height:144px;background:var(--white);box-shadow:0 2px 10px rgba(0,0,0,.12)}
.blog-sm .ph{position:absolute;left:0;top:0;width:195px;height:144px;border-radius:0 40px 0 0}
.blog-sm .txt{position:absolute;left:218px;top:18px;width:240px}
.blog-sm h3{font-size:18px;font-weight:700;line-height:23px;margin:8px 0 6px}

/* footer */
.footer{left:0;top:4012px;width:1200px;height:371px;background:var(--footer);color:var(--white)}
.f-brand{left:99px;top:80px;width:210px;text-align:center}
.f-brand .mark{width:86px;height:86px;border-radius:50%;border:4px solid var(--white);margin:0 auto 14px}
.f-brand .name{font-size:30px;font-weight:700;letter-spacing:4px;line-height:1}
.socials{display:flex;justify-content:center;gap:9px;margin-top:14px}
.socials i{display:block;width:38px;height:38px;border:1.5px solid var(--white);border-radius:50%}
.fcol{position:absolute;top:70px}
.fcol h4{font-size:18px;font-weight:700;margin-bottom:14px;text-transform:uppercase;border-bottom:2px solid var(--gold);display:inline-block;padding-bottom:2px}
.fcol li{list-style:none;font-size:13px;line-height:25.5px}
.contact-line{display:flex;gap:8px;font-size:13px;line-height:21px;margin-bottom:12px}
.f-rule{left:99px;top:308px;width:1002px;height:1px;background:#444}
.copyright{left:0;top:331px;width:1200px;text-align:center;font-size:13px}
</style>
</head>
<body>

<header>
  <div class="abs topbar">
    <span><svg width="14" height="14" viewBox="0 0 24 24"><path fill="#fff" d="M6.6 10.8a15 15 0 006.6 6.6l2.2-2.2c.3-.3.7-.4 1-.2 1.1.4 2.3.6 3.6.6.6 0 1 .4 1 1V20c0 .6-.4 1-1 1A17 17 0 013 4c0-.6.4-1 1-1h3.5c.6 0 1 .4 1 1 0 1.3.2 2.5.6 3.6.1.3 0 .7-.2 1z"/></svg>+1 555 - 014 -2290</span>
    <span><svg width="16" height="12" viewBox="0 0 16 12"><rect x="0.5" y="0.5" width="15" height="11" fill="none" stroke="#fff"/><path d="M1 1l7 6 7-6" fill="none" stroke="#fff"/></svg>info@brantmoorwealth.com</span>
    <span><svg width="16" height="16" viewBox="0 0 16 16"><circle cx="8" cy="8" r="7.3" fill="none" stroke="#fff"/><circle cx="8" cy="6.3" r="2.5" fill="#fff"/><path d="M3.5 13a5 4 0 019 0" fill="#fff"/></svg>Client Login</span>
  </div>
  <div class="abs brand"><div class="brand-mark"></div><div class="brand-name">BRANTMOOR</div></div>
  <nav class="abs nav"><span class="active">HOME</span><span>WHAT WE DO</span><span>WHO WE ARE</span><span>INSIGHTS</span></nav>
  <div class="btn nav-cta">Contact Us</div>
</header>

<section class="abs hero" role="img" aria-label="Photo of a smiling financial advisor in a suit meeting clients"></section>
<h1 class="abs hero-title">BRANTMOOR WEALTH</h1>
<p class="abs hero-text">Lorem ipsum dolor sit amet, consectetur adiping elit, sed do eiusmod tempor incididunt ut labore et dolore</p>
<div class="btn hero-btn">Find an Advisor</div>
<form class="abs form">
  <div class="form-head">REQUEST CONSULTATION</div>
  <div class="field" style="top:56px">Name</div>
  <div class="field" style="top:107px">Email</div>
  <div class="field" style="top:158px">Phone</div>
  <div class="field" style="top:208px;display:flex;justify-content:space-between">Best Day/ (Time of the week for consultaion)<svg width="10" height="10" viewBox="0 0 10 10"><path d="M1 3h8L5 8z" fill="#555"/></svg></div>
  <div class="field" style="top:258px;height:92px">Message</div>
  <div class="btn" style="left:14px;top:368px;width:322px;height:38px">Send us a message</div>
</form>
<div class="abs dots"><i></i><i class="on"></i><i></i><i></i></div>

<section>
  <div class="abs about-img" role="img" aria-label="Photo of hands around coin stacks with growing trees"></div>
  <div class="abs about-copy">
    <div class="eyebrow">Who we are</div>
    <h2>Wecome to Brantmoor Wealth</h2>
    <p>Lorem ipsum dolor sit amet, consectetur adipiscing elit,&nbsp; dsod tempor incididunt ut labore et dolore magna aliqua. Quis ipsum suspendisse ultrices gravida. Risus commodo viverra maecenas accumsan lacus vel facilisis.</p>
    <p>Lorem ipsum dolor sit amet, consectetur adipiscing elit,&nbsp; dsod tempor incididunt ut labore et dolore magna aliqua. Quis ipsum suspendisse ultrices gravida.</p>
  </div>
  <div class="btn about-btn">Learn More</div>
</section>

<section class="abs services">
  <div class="eyebrow abs center" style="top:55px">Our Services</div>
  <h2 class="section-title abs center" style="top:75px">What we offer</h2>
  <svg class="arrow" style="left:55px" width="30" height="14" viewBox="0 0 30 14"><path d="M29 7H2M8 1L2 7l6 6" fill="none" stroke="#333" stroke-width="1.6"/></svg>
  <svg class="arrow" style="left:1114px" width="30" height="14" viewBox="0 0 30 14"><path d="M1 7h27M22 1l6 6-6 6" fill="none" stroke="#333" stroke-width="1.6"/></svg>
  <div class="svc" style="left:99px"><div class="icon"></div><h3>Financial Planning</h3><p>Lorem ipsum dolor sit amet, chctetur adipiscing elit, sedo eiusmod tempor incididunt ut labore</p><div class="go"></div></div>
  <div class="svc" style="left:354px"><div class="icon"></div><h3>Business Ownership</h3><p>Lorem ipsum dolor sit amet, chctetur adipiscing elit, sedo eiusmod tempor incididunt ut labore</p><div class="go"></div></div>
  <div class="svc" style="left:609px"><div class="icon"></div><h3>Retirement Planning</h3><p>Lorem ipsum dolor sit amet, chctetur adipiscing elit, sedo eiusmod tempor incididunt ut labore</p><div class="go"></div></div>
  <div class="svc" style="left:864px"><div class="icon"></div><h3>Insurance</h3><p>Lorem ipsum dolor sit amet, chctetur adipiscing elit, sedo eiusmod tempor incididunt ut labore</p><div class="go"></div></div>
  <div class="btn all-btn">View all services</div>
</section>

<section class="abs cta" role="img" aria-label="Photo of a grey-haired advisor in a navy suit talking with a client">
  <div class="abs cta-circle">
    <div class="eyebrow">Get Started</div>
    <h2>We are Specialize in wealth management to better server</h2>
    <div class="btn cta-btn">Find an Advisor</div>
  </div>
</section>

<section>
  <div class="eyebrow abs center" style="top:2354px">Our Services</div>
  <h2 class="section-title abs center" style="top:2374px">Who we serve</h2>
  <div class="serve" style="left:99px;background:linear-gradient(180deg,#c9d0d6,#3d4650)" role="img" aria-label="Photo of two businessmen talking"><h3>Business Owners<br>&amp; Executives</h3><p>Lorem ipsum dolor sit amet, chctetur adipiscing elit, sedo</p></div>
  <div class="serve" style="left:355px;background:linear-gradient(180deg,#d9d3c8,#5a6a7e)" role="img" aria-label="Photo of a senior couple at home"><h3>Pre-<br>Retirees</h3><p>Lorem ipsum dolor sit amet, chctetur adipiscing elit, sedo</p></div>
  <div class="serve" style="left:610px;background:linear-gradient(180deg,#bfbfbd,#2d2f33)" role="img" aria-label="Photo of people working at laptops in an office"><h3>Private<br>Client</h3><p>Lorem ipsum dolor sit amet, chctetur adipiscing elit, sedo</p></div>
  <div class="serve" style="left:866px;background:linear-gradient(180deg,#d7d2c9,#8a7d6f)" role="img" aria-label="Photo of a smiling young woman"><h3>Young<br>Investor</h3><p>Lorem ipsum dolor sit amet, chctetur adipiscing elit, sedo</p></div>
</section>

<section class="abs testi">
  <div class="eyebrow abs center" style="top:64px">Testimonials</div>
  <h2 class="section-title abs center" style="top:84px">What our clients say</h2>
  <div class="tcard" style="left:99px"><div class="q">“</div><h4>John Smith</h4><small>Finibus Bonorum</small><p>Lorem ipsum dolor sit ectetur ipiscing elit, sed do or incididunt ut labore et dolorealiqua. Quis ipsum spendisse ultrices graviodo viverra maecenas accumsan lacus vel facilisis.</p></div>
  <div class="tcard" style="left:444px"><div class="q">“</div><h4>John Smith</h4><small>Finibus Bonorum</small><p>Lorem ipsum dolor sit ectetur ipiscing elit, sed do or incididunt ut labore et dolorealiqua. Quis ipsum spendisse ultrices graviodo viverra maecenas accumsan lacus vel facilisis.</p></div>
  <div class="tcard" style="left:788px"><div class="q">“</div><h4>John Smith</h4><small>Finibus Bonorum</small><p>Lorem ipsum dolor sit ectetur ipiscing elit, sed do or incididunt ut labore et dolorealiqua. Quis ipsum spendisse ultrices graviodo viverra maecenas accumsan lacus vel facilisis.</p></div>
</section>

<section>
  <div class="eyebrow abs center" style="top:3382px">Resource</div>
  <h2 class="section-title abs center" style="top:3402px">Latest Blog</h2>
  <article class="abs blog-main">
    <div class="ph" role="img" aria-label="Photo of business people shaking hands in an office"></div>
    <div class="body">
      <div class="date">30, Aug 2023</div>
      <h3>Seasons of Patient Growth", written by Aurel Vantis in 45 BC</h3>
      <p>Lorem ipsum dolor sit amet, consectetur adipiscing elit, sed do eiusmod tempor incididunt ut labore et dolore</p>
      <span class="more">READ MORE</span>
    </div>
  </article>
  <article class="blog-sm" style="top:3464px"><div class="ph" style="background:linear-gradient(135deg,#0e2a4a,#2f6b8f)" role="img" aria-label="Photo of a woman viewing a city at night"></div><div class="txt"><div class="date">30, Aug 2023</div><h3>The standard Lorem Ipsum passage, used since</h3><span class="more">READ MORE</span></div></article>
  <article class="blog-sm" style="top:3622px"><div class="ph" style="background:linear-gradient(135deg,#c7c2b6,#3b3a36)" role="img" aria-label="Photo of coin stacks on a board"></div><div class="txt"><div class="date">30, Aug 2023</div><h3>The standard Lorem Ipsum passage, used since</h3><span class="more">READ MORE</span></div></article>
  <article class="blog-sm" style="top:3779px"><div class="ph" style="background:linear-gradient(135deg,#e8ecef,#c9a98a)" role="img" aria-label="Photo of wooden blocks with insurance symbols"></div><div class="txt"><div class="date">30, Aug 2023</div><h3>The standard Lorem Ipsum passage, used since</h3><span class="more">READ MORE</span></div></article>
</section>

<footer class="abs footer">
  <div class="abs f-brand">
    <div class="mark"></div>
    <div class="name">BRANTMOOR</div>
    <div class="socials"><i></i><i></i><i></i><i></i></div>
  </div>
  <div class="fcol" style="left:421px"><h4>Quick Links</h4><ul><li>Home</li><li>About Us</li><li>Product</li><li>Markets</li><li>Services</li><li>News</li></ul></div>
  <div class="fcol" style="left:649px"><h4>Insights</h4><ul><li>Your Money</li><li>Your Business</li><li>Your Retirement</li><li>Your Legacy</li><li>Your Freedom</li><li>Market &amp; Investments</li><li>In the News</li></ul></div>
  <div class="fcol" style="left:872px"><h4>Contact Us</h4>
    <div class="contact-line"><svg width="14" height="18" viewBox="0 0 14 18"><path d="M7 17s6-6.5 6-10.5A6 6 0 001 6.5C1 10.5 7 17 7 17z" fill="none" stroke="#fff"/><circle cx="7" cy="6.5" r="2" fill="none" stroke="#fff"/></svg><span>123 Your Adress Goes Here.<br>AU, 1234567</span></div>
    <div class="contact-line"><svg width="14" height="14" viewBox="0 0 24 24"><path fill="none" stroke="#fff" stroke-width="2" d="M6.6 10.8a15 15 0 006.6 6.6l2.2-2.2c.3-.3.7-.4 1-.2 1.1.4 2.3.6 3.6.6.6 0 1 .4 1 1V20c0 .6-.4 1-1 1A17 17 0 013 4c0-.6.4-1 1-1h3.5c.6 0 1 .4 1 1 0 1.3.2 2.5.6 3.6.1.3 0 .7-.2 1z"/></svg><span>+1 555 014 2290</span></div>
    <div class="contact-line"><svg width="16" height="12" viewBox="0 0 16 12"><rect x="0.5" y="0.5" width="15" height="11" fill="none" stroke="#fff"/><path d="M1 1l7 6 7-6" fill="none" stroke="#fff"/></svg><span>info@brantmoorwealth.com</span></div>
  </div>
  <div class="abs f-rule"></div>
  <div class="abs copyright">Copyright © 2023 brantmoorwealth.com. All rights reserved.</div>
</footer>

</body>
</html>
```